Builder Business Card Design

I need a design a business card that is different from others and use as a logo for other prints. I'm a builder that build domestic/residential home new, renovate & malty unit development . I would like a Slogan that in unique . I look forward to talk to someone about it.

Industry/Entity Type

Business

Contact Information for Business Card

Tallowbrook homes, Colin Marchetti 0487 512 904 , DB-U 74129

```html
<!DOCTYPE html>
<html lang="en">
<head>
<meta charset="utf-8">
<title>Tallowbrook Homes – Business Card</title>
<link rel="stylesheet" href="https://fonts.googleapis.com/css2?family=Cinzel:wght@400;500&display=swap">
<style>
  :root {
    --backdrop-centre: #ffffff;
    --backdrop-edge: #d9d9d9;
    --band-orange: #e67a1e;
    --band-dark: #463331;
    --frame-white: #ffffff;
    --card-brown: #6c3e35;
    --text-light: #ffffff;
  }
  html, body {
    margin: 0;
    padding: 0;
    width: 1200px;
    height: 928px;
    overflow: hidden;
  }
  body {
    position: relative;
    background: radial-gradient(ellipse at 50% 48%, var(--backdrop-centre) 0%, var(--backdrop-centre) 35%, var(--backdrop-edge) 100%);
    font-family: "Cinzel", "Trajan Pro", serif;
  }
  .band {
    position: absolute;
    left: 285px;
    width: 629px;
  }
  .band--orange {
    top: 281px;
    height: 170px;
    background: var(--band-orange);
  }
  .band--dark {
    top: 477px;
    height: 168px;
    background: var(--band-dark);
  }
  .card-frame {
    position: absolute;
    left: 318px;
    top: 304px;
    width: 559px;
    height: 341px;
    background: var(--frame-white);
  }
  .card-face {
    position: absolute;
    left: 338px;
    top: 324px;
    width: 520px;
    height: 321px;
    background: var(--card-brown);
    color: var(--text-light);
    text-align: center;
  }
  .brand-name {
    position: absolute;
    left: 0;
    right: 0;
    top: 168px;
    margin: 0;
    font-weight: 400;
    font-size: 30px;
    letter-spacing: 0.5px;
    line-height: 1;
  }
  .contact-line {
    position: absolute;
    left: 0;
    right: 0;
    top: 290px;
    margin: 0;
    font-size: 14.5px;
    font-weight: 400;
    letter-spacing: 0.3px;
    line-height: 1;
  }
</style>
</head>
<body>
  <div class="band band--orange"></div>
  <div class="band band--dark"></div>
  <div class="card-frame"></div>
  <section class="card-face">
    <h1 class="brand-name">Tallowbrook Homes</h1>
    <p class="contact-line">Colin Marchetti 0487 512 904 , DB-U 74129</p>
  </section>
</body>
</html>
```